Website plus logo for a finance business (in Wix)

We need a revamp of our website and our logo - visit www.halvernbridging.com for the current site.

We are a relatively new finance firm, providing short term (bridging) loans to property developers and other businesses in the UK.

Most of the information will go on the homepage. The other 3 or 4 pages are relatively basic. If you felt it was appropriate, the information on page 2 (case studies) could be incorporated on page 1.

The current website isn't too bad and gives you an idea of the information we would like covering on the website and in what order.

The logo should be clean, simple and modern, probably branded around a rocket. The current logo is a good starting point. The word rocket should be the focal point though.

The main header colour scheme should be similar to the current website (deep purples) but we would consider dark blues or reds. An example of a palette of colours we really like is attached.

The style should be modern and clean. Lots of whites and background space but with an underlying warmth, suggesting trust and reliability.

Examples of good brands and websites that we like in our sector are www.brindlefunds.com, www.quarlowlending.co.uk and www.veltrope.co.uk - we particularly like Veltrope.

Important note - as part of the service, the website designer must be able to create the website in Wix once the design is approved. Our current website is through Wix and we want to keep it that way.

Therefore, once the design is approved, as part of the finalisation process, the designer will need to create the website in our existing Wix account.

This will also involve creating a mobile friendly version of the site (which is more or less automatic in Wix anyway). None of this should be difficult as Wix is very easy to use.

Thanks for your interest!

Kind regards

HalvernBridging

Target Market(s)

Small to medium property developers and businesses in the North West of the UK

Industry/Entity Type

Finance

Contact Information for Business Card

One side just feature the logo against a strong background colour.
The other side should have a nice clean look about it, with the details of our sales director, Tessa Marwick.
tessa@halvernbridging.com
0161 555 0193
07700 900418

Logo Text

Halvern Bridging

Coding

Coded - Design and coding required

Number of Pages Required

4 page

Font styles to use
Sans Serif

Colors
6b449b
0456a4

Requirements
Must have
• Clean looking home page, modelled on the examples that we've given.
• The start of the home page must make it clear what we do - this could be achieved by rotating banners.
• Must be produced in Wix once the design is approved.
• Should follow example colour palette given.
Nice to have
• Parallax pictures
Should not have
• Old fashioned or traditional styling - we do not want to look like an accountant or law firm's website

```html
<!DOCTYPE html>
<html lang="en">
<head>
<meta charset="utf-8">
<title>Halvern Bridging</title>
<link href="https://fonts.googleapis.com/css2?family=Montserrat:wght@400;500;600;700&family=Open+Sans:wght@400;600&display=swap" rel="stylesheet">
<style>
:root{
  --purple:#6b449b;
  --purple-deep:#5a2d91;
  --blue:#0456a4;
  --navy:#1d3f8f;
  --ink:#1c1c1c;
  --text:#3a3a3a;
  --muted:#8a8a8a;
  --light:#f2f2f2;
  --line:#d6d6d6;
  --white:#ffffff;
  --map:#e4e7ea;
}
*{box-sizing:border-box;margin:0;padding:0}
html,body{width:1200px;height:4317px;overflow:hidden}
body{font-family:"Open Sans",Arial,sans-serif;color:var(--text);background:var(--white);position:relative}
h1,h2,h3,.nav,.stat{font-family:"Montserrat",Arial,sans-serif}

/* hero */
.hero{position:absolute;left:0;top:0;width:1200px;height:700px;background:linear-gradient(120deg,#7d7068 0%,#a09488 35%,#6f665f 65%,#3e3a38 100%)}
.hero-photo{position:absolute;inset:0}
.hero-shade{position:absolute;inset:0;background:rgba(30,30,35,.35)}
.brand{position:absolute;left:98px;top:42px;display:flex;align-items:center;gap:12px;color:var(--white);font-family:"Montserrat",sans-serif;font-weight:600;font-size:26px;letter-spacing:.5px}
.brand-dot{width:30px;height:30px;border-radius:50%;background:var(--white)}
.nav{position:absolute;right:98px;top:60px;display:flex;gap:30px;font-size:15px;font-weight:600;color:var(--white);letter-spacing:.4px}
.hero-title{position:absolute;left:0;width:1200px;top:362px;text-align:center;color:var(--white);font-weight:600}
.hero-title .small{display:block;font-size:40px;letter-spacing:1.5px}
.hero-title .big{display:block;font-size:58px;margin-top:2px;letter-spacing:1px}
.hero-arrow{position:absolute;left:570px;top:492px}

/* shared heading */
.section-title{position:absolute;left:0;width:1200px;text-align:center;font-size:35px;font-weight:600;color:var(--ink);letter-spacing:1px}
.rule{position:absolute;left:566px;width:68px;height:4px;background:var(--blue)}

/* services */
.card{position:absolute;top:892px;width:242px;height:398px;background:var(--light);box-shadow:0 2px 4px rgba(0,0,0,.18)}
.card-img{height:202px}
.card h3{font-size:22px;font-weight:500;color:var(--ink);margin:22px 16px 10px}
.card p{font-size:13.5px;line-height:23px;margin:0 16px;color:var(--text)}

/* about */
.about{position:absolute;left:0;top:1399px;width:1200px;height:544px;background:#eeeeee}
.about-img{position:absolute;left:633px;top:0;width:567px;height:544px;background:linear-gradient(160deg,#7fa7d8 0%,#c9dcf0 45%,#2c2c30 75%,#121214 100%)}
.about h2{position:absolute;left:98px;top:92px;font-size:35px;font-weight:600;color:var(--ink)}
.about .rule{left:98px;top:150px;width:68px}
.about-text{position:absolute;left:98px;top:186px;width:500px;font-size:14px;line-height:25px}
.about-text p{margin-bottom:14px}
.btn{position:absolute;display:flex;align-items:center;justify-content:center;background:var(--navy);color:var(--white);font-family:"Montserrat",sans-serif;font-size:12.5px;font-weight:600;border-radius:3px}

/* stats */
.stats{position:absolute;left:0;top:1943px;width:1200px;height:175px;background:linear-gradient(90deg,#1f3f97 0%,#3b3a9e 45%,#5a2d91 100%)}
.stat{position:absolute;top:40px;width:200px;text-align:center;color:var(--white)}
.stat b{display:block;font-size:33px;font-weight:500}
.stat span{display:block;font-size:17px;line-height:25px;font-weight:500;margin-top:6px}
.divider{position:absolute;top:58px;width:2px;height:60px;background:rgba(255,255,255,.45)}

/* case studies */
.case{position:absolute;width:397px;height:331px}
.case-quote{background:var(--purple);color:var(--white);text-align:center;font-size:15px;line-height:26px;padding:38px 40px 0}
.case-quote .mark{font-family:"Montserrat",sans-serif;font-size:72px;line-height:50px;font-weight:700}
.case-quote p{margin-top:14px}

/* clients */
.clients{position:absolute;left:0;top:3097px;width:1200px;height:256px;background:var(--light)}
.client{position:absolute;top:153px;font-family:"Montserrat",sans-serif;font-size:24px;font-weight:600;color:#9a9a9a;text-align:center;width:160px;white-space:nowrap}

/* contact */
.map{position:absolute;left:98px;top:3485px;width:1004px;height:259px;background:var(--map)}
.map-notch{position:absolute;left:580px;top:3744px;width:0;height:0;border-left:14px solid transparent;border-right:14px solid transparent;border-top:14px solid var(--map)}
.col-title{position:absolute;top:3805px;font-family:"Montserrat",sans-serif;font-size:30px;font-weight:600;color:var(--ink)}
.field{position:absolute;left:98px;width:397px;height:38px;border:1px solid #bfbfbf;font-size:12px;font-style:italic;color:#6a6a6a;padding:10px 12px}
.office-intro{position:absolute;left:568px;top:3874px;width:380px;font-size:16px;line-height:22px;color:var(--text)}
.office-row{position:absolute;left:568px;display:flex;gap:16px;align-items:flex-start;font-size:13.5px;line-height:19px}
.office-row svg{flex:none;margin-top:1px}

/* footer */
.footer-line{position:absolute;left:0;top:4236px;width:1200px;height:1px;background:var(--line)}
.copyright{position:absolute;left:98px;top:4266px;font-size:13px;color:var(--text)}
.social{position:absolute;top:4264px;width:22px;height:22px;border:1px solid #555;border-radius:50%}
</style>
</head>
<body>

<header class="hero">
  <div class="hero-photo" role="img" aria-label="Photo of business people shaking hands across a desk in a bright office"></div>
  <div class="hero-shade"></div>
  <div class="brand"><span class="brand-dot"></span>Halvern Bridging</div>
  <nav class="nav"><span>HOME</span><span>SERVICES</span><span>CLIENTS</span><span>HOW CAN WE HELP?</span><span>ABOUT</span><span>CONTACT</span></nav>
  <h1 class="hero-title"><span class="small">BRIDGE FUNDING,</span><span class="big">THE MODERN WAY</span></h1>
  <svg class="hero-arrow" width="60" height="34" viewBox="0 0 60 34"><polyline points="3,3 30,30 57,3" fill="none" stroke="#fff" stroke-width="4"/></svg>
</header>

<h2 class="section-title" style="top:760px">HOW CAN WE HELP?</h2>
<div class="rule" style="top:833px"></div>

<article class="card" style="left:98px">
  <div class="card-img" role="img" aria-label="Photo of a businessman on stacked coins" style="background:linear-gradient(160deg,#4d6d8c,#8aa3b8)"></div>
  <h3>Bridging loans</h3>
  <p>Do you need to put in place temporary funding whilst you organise a long term strategy? Halvern can provide bridge funding on a wide range.</p>
</article>
<article class="card" style="left:354px">
  <div class="card-img" role="img" aria-label="Photo of a hand signing papers beside a model house" style="background:linear-gradient(160deg,#2e2a26,#b9a58a)"></div>
  <h3>Auction Purchases</h3>
  <p>Thinking of bidding? Won a property? Halvern is able to swiftly fund the purchase of an auction property whilst you organise long term funding.</p>
</article>
<article class="card" style="left:607px">
  <div class="card-img" role="img" aria-label="Photo of people reviewing charts at a desk" style="background:linear-gradient(160deg,#6b6f58,#d5d2c4)"></div>
  <h3>Development</h3>
  <p>Halvern can provide finance to help with the development of property. We can supply the acquisition funding and/or a facility to be drawn down as work progresses.</p>
</article>
<article class="card" style="left:863px">
  <div class="card-img" role="img" aria-label="Photo of a business meeting at a table" style="background:linear-gradient(160deg,#5a5656,#cfc9c3)"></div>
  <h3>Business loans</h3>
  <p>Do you want to grow your business? We provide short term facilities allowing you to achieve your ambitions.</p>
</article>

<section class="about">
  <h2>ABOUT OUR COMPANY</h2>
  <div class="rule"></div>
  <div class="about-text">
    <p>Halvern Bridging is a Manchester-based bridging loan provider, covering property purchases, developments and general business needs.</p>
    <p>We are not a broker. We fund you with our own money. When you speak to us, you speak with the decision-maker.</p>
    <p>We do not have strict lending parameters. We pride ourselves on working out an individual deal for each client. We can find solutions for most clients, large or small.</p>
  </div>
  <div class="btn" style="left:98px;top:420px;width:118px;height:32px">READ MORE</div>
  <div class="about-img" role="img" aria-label="Photo of a businessman holding a model of city towers on a patch of grass"></div>
</section>

<section class="stats">
  <div class="stat" style="left:185px"><b>2023</b><span>Year<br>Established</span></div>
  <div class="divider" style="left:399px"></div>
  <div class="stat" style="left:407px"><b>206</b><span>Projects<br>Completed</span></div>
  <div class="divider" style="left:613px"></div>
  <div class="stat" style="left:620px"><b>870</b><span>Business<br>Environment</span></div>
  <div class="divider" style="left:843px"></div>
  <div class="stat" style="left:835px"><b>26</b><span>Awards<br>Won</span></div>
</section>

<h2 class="section-title" style="top:2193px">CASE STUDIES</h2>
<div class="rule" style="top:2257px"></div>

<div class="case case-quote" style="left:201px;top:2314px">
  <div class="mark">&#8221;</div>
  <p>Halvern was able to assist this growing Yorkshire-based manufacturing business with a bridging loan to help fund the expansion of its factory.</p>
  <p>Amount of funding: &pound;655,000<br>Duration: 10 months<br>LTV: 78%<br>Interest rate pcm: 0.9%</p>
</div>
<div class="case" style="left:604px;top:2314px;background:linear-gradient(150deg,#6f7a6a,#9aa08f,#5d6558)" role="img" aria-label="Aerial photo of a housing estate"></div>
<div class="case" style="left:201px;top:2654px;background:linear-gradient(170deg,#5a3a30,#b8683e,#8a6a58)" role="img" aria-label="Photo of a building interior under refurbishment"></div>
<div class="case" style="left:604px;top:2654px;background:linear-gradient(170deg,#2e3a2c,#5b5a52,#c79a5a)" role="img" aria-label="Photo of a modern house at dusk"></div>

<section class="clients">
  <h2 class="section-title" style="top:45px">OUR CLIENTS</h2>
  <div class="client" style="left:87px">KESTON</div>
  <div class="client" style="left:231px">Morvale</div>
  <div class="client" style="left:401px">TRENMOOR</div>
  <div class="client" style="left:568px">Linwick</div>
  <div class="client" style="left:744px">ashby</div>
  <div class="client" style="left:916px">DRAYLE</div>
</section>

<h2 class="section-title" style="top:3402px">CONTACT US</h2>
<div class="map" role="img" aria-label="Street map showing the office location"></div>
<div class="map-notch"></div>

<h3 class="col-title" style="left:98px">Inquiries</h3>
<div class="field" style="top:3875px">Your first name</div>
<div class="field" style="top:3921px">Your email</div>
<div class="field" style="top:3967px">Your Phone</div>
<div class="field" style="top:4013px;height:108px">Message</div>
<div class="btn" style="left:98px;top:4139px;width:132px;height:31px">SUBMIT</div>

<h3 class="col-title" style="left:561px">Head Office</h3>
<p class="office-intro">To explore how we can help you communicate better, please be in touch!</p>
<div class="office-row" style="top:3940px"><svg width="16" height="22" viewBox="0 0 16 22"><path d="M8 0C3.6 0 0 3.5 0 7.8 0 13.6 8 22 8 22s8-8.4 8-14.2C16 3.5 12.4 0 8 0zm0 11a3 3 0 1 1 0-6 3 3 0 0 1 0 6z" fill="#222"/></svg><span>Halvern Bridging Limited<br>Weaver Mill, Brook Lane, Rochdale, OL11<br>4QT</span></div>
<div class="office-row" style="top:4010px"><svg width="16" height="20" viewBox="0 0 16 20"><rect x="2" y="0" width="12" height="20" rx="2" fill="#222"/><rect x="4" y="3" width="8" height="12" fill="#fff"/></svg><span>Main: &nbsp;0161 555 0193</span></div>
<div class="office-row" style="top:4054px"><svg width="18" height="14" viewBox="0 0 18 14"><rect width="18" height="14" rx="1" fill="#222"/><polyline points="1,1 9,8 17,1" fill="none" stroke="#fff" stroke-width="1.5"/></svg><span>Email: &nbsp;info@halvernbridging.com</span></div>
<div class="office-row" style="top:4098px"><svg width="18" height="18" viewBox="0 0 18 18"><rect x="0" y="5" width="18" height="13" rx="2" fill="#222"/><rect x="4" y="0" width="10" height="7" fill="#222"/><rect x="4" y="9" width="10" height="2" fill="#fff"/></svg><span>Fax: (852) 5550 1274</span></div>

<div class="footer-line"></div>
<p class="copyright">&copy;2018 Halvern Bridging, All Rights Reserved.</p>
<span class="social" style="left:992px"></span>
<span class="social" style="left:1018px"></span>
<span class="social" style="left:1044px"></span>
<span class="social" style="left:1070px"></span>

</body>
</html>
```